Business card for travel services company showing company name (VEMTIRO ONLINE SERVICES LLC), 4 contact numbers, website which is [login to view URL], Facebook @vemtirocom, Instagram @vemtirocom and Twitter @vemtiroC accounts, 2 mail ID , 2 address location, the services (Flights, hotels booking, Transfer, sightseeing, car rentals, cruise, Visa)

```html
<!DOCTYPE html>
<html lang="en">
<head>
<meta charset="utf-8">
<title>Vemtiro Online Services LLC – Business Card</title>
<link href="https://fonts.googleapis.com/css2?family=Jost:wght@400;500;600;700&display=swap" rel="stylesheet">
<style>
  :root {
    --bg: #d9d9d9;
    --ink: #1a1a1a;
    --brand: #1d4f8f;
    --accent: #e8572a;
    --white: #ffffff;
    --link: #1d3f9c;
    --navy: #1f2e6e;
    --band: rgba(36, 128, 190, 0.86);
    --back-top: #1b4f9c;
    --back-bottom: #2a6fb8;
  }
  * { box-sizing: border-box; margin: 0; padding: 0; }
  html, body {
    width: 1200px; height: 871px; overflow: hidden;
    background: var(--bg);
    font-family: "Jost", sans-serif;
  }
  .canvas { position: relative; width: 1200px; height: 871px; }

  .card {
    position: absolute; top: 50px;
    width: 440px; height: 770px;
    overflow: hidden;
    background: var(--white);
    box-shadow: 0 6px 18px rgba(0,0,0,0.18);
  }
  .card--front { left: 140px; }
  .card--back { left: 620px; background: linear-gradient(180deg, var(--back-top), var(--back-bottom)); }

  /* front */
  .beach-photo {
    position: absolute; inset: 0;
    background: linear-gradient(180deg,
      #4f86c6 0%, #7fb0e0 25%, #a9cdec 38%,
      #2f9fc4 44%, #3cc0c8 55%, #8fdad6 66%,
      #e6f1ee 76%, #f3f1ea 100%);
  }
  .brand {
    position: absolute; left: 40px; top: 170px;
    display: flex; align-items: center; gap: 10px;
  }
  .brand__mark { width: 22px; height: 22px; border-radius: 50%; background: var(--accent); }
  .brand__name {
    font-weight: 600; font-size: 22px; color: var(--brand);
    letter-spacing: 0.2px;
  }
  .section-title {
    position: absolute; left: 40px;
    color: var(--white); font-weight: 500; font-size: 27px;
  }
  .card--front .section-title { top: 290px; }

  .contact-list {
    position: absolute; left: 40px; right: 20px; top: 340px;
    list-style: none;
  }
  .contact {
    display: flex; align-items: center; gap: 16px;
    color: var(--ink); font-size: 15.5px; line-height: 1.2;
    margin-bottom: 13px;
  }
  .contact__icon {
    flex: 0 0 30px; width: 30px; height: 30px;
    background: var(--ink); border-radius: 3px;
    display: flex; align-items: center; justify-content: center;
  }
  .contact__icon svg { width: 18px; height: 18px; }
  .website {
    position: absolute; left: 0; right: 0; bottom: 30px;
    text-align: center; color: var(--link); font-weight: 600; font-size: 18px;
  }

  /* back */
  .landmark-photo {
    position: absolute; left: 200px; top: 110px; right: 0; bottom: 0;
    background: linear-gradient(180deg, #3b6fb4 0%, #6d8fb8 45%, #5f8f70 78%, #4f9a3a 100%);
  }
  .card--back .brand { top: 38px; left: 30px; }
  .card--back .brand__name { color: var(--white); }
  .card--back .section-title { top: 100px; left: 30px; font-weight: 600; }

  .services {
    position: absolute; left: 0; right: 0; top: 150px;
    list-style: none;
  }
  .service {
    display: flex; align-items: center;
    height: 46px; margin-bottom: 6px;
  }
  .service__icon {
    flex: 0 0 56px; height: 100%;
    background: var(--navy);
    display: flex; align-items: center; justify-content: center;
  }
  .service__icon svg { width: 28px; height: 28px; }
  .service__label {
    flex: 1; height: 100%;
    background: var(--band);
    color: var(--white); font-weight: 600; font-size: 25px;
    display: flex; align-items: center; padding-left: 70px;
  }
</style>
</head>
<body>
<main class="canvas">

  <section class="card card--front" aria-label="Business card front">
    <div class="beach-photo" role="img" aria-label="Photo of a tropical beach with blue sky, turquoise sea and white sand"></div>

    <div class="brand">
      <span class="brand__mark"></span>
      <span class="brand__name">Vemtiro Online Services LLC</span>
    </div>

    <h2 class="section-title">Contact Us:</h2>

    <ul class="contact-list">
      <li class="contact">
        <span class="contact__icon">
          <svg viewBox="0 0 24 24"><path d="M12 2a7 7 0 0 0-7 7c0 5 7 13 7 13s7-8 7-13a7 7 0 0 0-7-7zm0 9.5A2.5 2.5 0 1 1 12 6.5a2.5 2.5 0 0 1 0 5z" fill="#fff"/></svg>
        </span>
        <span>Office 12, Level 3, Coral Media Park,<br>Marisa, UAE<br>B. 217 S. 14 Nadira, Osman Tarek<br>St. Port Halim, Sudan</span>
      </li>
      <li class="contact">
        <span class="contact__icon">
          <svg viewBox="0 0 24 24"><path d="M6.6 10.8a15 15 0 0 0 6.6 6.6l2.2-2.2a1 1 0 0 1 1-.25 11.4 11.4 0 0 0 3.6.57 1 1 0 0 1 1 1V20a1 1 0 0 1-1 1A17 17 0 0 1 3 4a1 1 0 0 1 1-1h3.5a1 1 0 0 1 1 1c0 1.25.2 2.45.57 3.57a1 1 0 0 1-.25 1z" fill="#fff"/></svg>
        </span>
        <span>+249100000120, +249100000333<br>+249100000777, +249100000888<br>+249900000629, +971500000402</span>
      </li>
      <li class="contact">
        <span class="contact__icon">
          <svg viewBox="0 0 24 24"><rect x="3" y="6" width="18" height="12" fill="none" stroke="#fff" stroke-width="2"/><path d="M3 6l9 7 9-7" fill="none" stroke="#fff" stroke-width="2"/></svg>
        </span>
        <span>info@vemtiro.com<br>support@vemtirocom</span>
      </li>
      <li class="contact">
        <span class="contact__icon">
          <svg viewBox="0 0 24 24"><circle cx="12" cy="12" r="8" fill="none" stroke="#fff" stroke-width="2"/><path d="M4 12h16M12 4c3 3 3 13 0 16M12 4c-3 3-3 13 0 16" fill="none" stroke="#fff" stroke-width="1.5"/></svg>
        </span>
        <span>@vemtirocom</span>
      </li>
      <li class="contact">
        <span class="contact__icon">
          <svg viewBox="0 0 24 24"><circle cx="12" cy="12" r="8" fill="none" stroke="#fff" stroke-width="2"/><path d="M4 12h16M12 4c3 3 3 13 0 16M12 4c-3 3-3 13 0 16" fill="none" stroke="#fff" stroke-width="1.5"/></svg>
        </span>
        <span>@vemtirocom</span>
      </li>
      <li class="contact">
        <span class="contact__icon">
          <svg viewBox="0 0 24 24"><circle cx="12" cy="12" r="8" fill="none" stroke="#fff" stroke-width="2"/><path d="M4 12h16M12 4c3 3 3 13 0 16M12 4c-3 3-3 13 0 16" fill="none" stroke="#fff" stroke-width="1.5"/></svg>
        </span>
        <span>@vemtiroC</span>
      </li>
    </ul>

    <p class="website">www.vemtiro.com</p>
  </section>

  <section class="card card--back" aria-label="Business card back">
    <div class="landmark-photo" role="img" aria-label="Photo of a landmark tower above a green park under a blue sky"></div>

    <div class="brand">
      <span class="brand__mark"></span>
      <span class="brand__name">Vemtiro Online Services LLC</span>
    </div>

    <h2 class="section-title">Our Services:</h2>

    <ul class="services">
      <li class="service"><span class="service__icon"><svg viewBox="0 0 28 28"><circle cx="14" cy="14" r="12" fill="none" stroke="#fff" stroke-width="2"/><path d="M9 9l10 5-10 5 3-5z" fill="#fff"/></svg></span><span class="service__label">Flights</span></li>
      <li class="service"><span class="service__icon"><svg viewBox="0 0 28 28"><circle cx="14" cy="14" r="12" fill="none" stroke="#fff" stroke-width="2"/><path d="M9 9l10 5-10 5 3-5z" fill="#fff"/></svg></span><span class="service__label">Buses</span></li>
      <li class="service"><span class="service__icon"><svg viewBox="0 0 28 28"><circle cx="14" cy="14" r="12" fill="none" stroke="#fff" stroke-width="2"/><path d="M9 9l10 5-10 5 3-5z" fill="#fff"/></svg></span><span class="service__label">Train</span></li>
      <li class="service"><span class="service__icon"><svg viewBox="0 0 28 28"><circle cx="14" cy="14" r="12" fill="none" stroke="#fff" stroke-width="2"/><path d="M9 9l10 5-10 5 3-5z" fill="#fff"/></svg></span><span class="service__label">Ferry</span></li>
      <li class="service"><span class="service__icon"><svg viewBox="0 0 28 28"><circle cx="14" cy="14" r="12" fill="none" stroke="#fff" stroke-width="2"/><path d="M9 9l10 5-10 5 3-5z" fill="#fff"/></svg></span><span class="service__label">Hotels</span></li>
      <li class="service"><span class="service__icon"><svg viewBox="0 0 28 28"><circle cx="14" cy="14" r="12" fill="none" stroke="#fff" stroke-width="2"/><path d="M9 9l10 5-10 5 3-5z" fill="#fff"/></svg></span><span class="service__label">Transfer</span></li>
      <li class="service"><span class="service__icon"><svg viewBox="0 0 28 28"><circle cx="14" cy="14" r="12" fill="none" stroke="#fff" stroke-width="2"/><path d="M9 9l10 5-10 5 3-5z" fill="#fff"/></svg></span><span class="service__label">Sightseeing</span></li>
      <li class="service"><span class="service__icon"><svg viewBox="0 0 28 28"><circle cx="14" cy="14" r="12" fill="none" stroke="#fff" stroke-width="2"/><path d="M9 9l10 5-10 5 3-5z" fill="#fff"/></svg></span><span class="service__label">Car Rentals</span></li>
      <li class="service"><span class="service__icon"><svg viewBox="0 0 28 28"><circle cx="14" cy="14" r="12" fill="none" stroke="#fff" stroke-width="2"/><path d="M9 9l10 5-10 5 3-5z" fill="#fff"/></svg></span><span class="service__label">Cruise</span></li>
      <li class="service"><span class="service__icon"><svg viewBox="0 0 28 28"><circle cx="14" cy="14" r="12" fill="none" stroke="#fff" stroke-width="2"/><path d="M9 9l10 5-10 5 3-5z" fill="#fff"/></svg></span><span class="service__label">Visa</span></li>
    </ul>
  </section>

</main>
</body>
</html>
```